Business Card for premium dental clinic

We are a premium dental clinic based in Brasov, Romania with more than 15 year on the market, providing quality dental treatment made by a team of more specialized dentists, working with modern equipment as a solution to beautiful and healthy teeth.

Our current logo for the clinic use 2 square with colors black and gold - dr Corbescu - studio, using family fonts Bodoni, Myriad Pro and Segoe Print.
Depending on the printing we used some gold CMYK background or gold foil picture background or a gold gradient.
We want a business card:
- eye catching business card
- distinguished business card
- premium design
- to keep the color scheme of black and gold
- to attract the customers to spent time reading the information
- modern concept

```html
<!DOCTYPE html>
<html lang="en">
<head>
<meta charset="UTF-8">
<title>dr Corbescu studio – business card</title>
<link rel="stylesheet" href="https://fonts.googleapis.com/css2?family=PT+Sans:wght@400;700&family=PT+Sans+Narrow:wght@700&family=Noto+Sans:wght@400&display=swap">
<style>
  :root {
    --backdrop: #e9e6e1;
    --card-black: #2b2b2b;
    --card-black-deep: #1f1f1f;
    --gold-light: #f6d777;
    --gold-mid: #e2b23a;
    --gold-deep: #b98a1c;
    --gold-text: #d8ac4a;
    --white: #ffffff;
    --ink: #2a2a2a;
  }
  * { margin: 0; padding: 0; box-sizing: border-box; }
  html, body { width: 1200px; height: 1200px; overflow: hidden; }
  body {
    background: var(--backdrop);
    font-family: "PT Sans", sans-serif;
    position: relative;
  }
  .card {
    position: absolute;
    left: 162px;
    width: 876px;
    height: 500px;
    background: linear-gradient(135deg, var(--card-black) 0%, var(--card-black-deep) 100%);
    overflow: hidden;
    box-shadow: 0 10px 30px rgba(0,0,0,0.18);
  }
  .card--front { top: 66px; }
  .card--back { top: 634px; }

  .gold-foil {
    position: absolute;
    background: linear-gradient(135deg, var(--gold-light) 0%, var(--gold-mid) 45%, var(--gold-deep) 75%, var(--gold-light) 100%);
  }

  /* front */
  .card--front .gold-foil { left: 0; top: 22px; width: 420px; height: 478px; }
  .rule {
    position: absolute;
    height: 4px;
    background: var(--white);
  }
  .rule--top { left: 420px; right: 0; top: 48px; }
  .rule--bottom { left: 420px; right: 0; top: 446px; }
  .name-plate {
    position: absolute;
    background: var(--white);
    color: var(--ink);
    display: flex;
    align-items: center;
    white-space: nowrap;
  }
  .card--front .name-plate {
    left: 110px; top: 120px; width: 310px; height: 120px;
    padding-left: 26px;
    font-size: 52px;
  }
  .brand-word {
    position: absolute;
    color: var(--white);
    font-family: "PT Sans Narrow", sans-serif;
    font-weight: 700;
    white-space: nowrap;
  }
  .card--front .brand-word--studio { left: 500px; top: 210px; font-size: 76px; }
  .card--front .brand-word--clinic { right: 40px; top: 360px; font-size: 44px; }

  /* back */
  .card--back .gold-foil { left: 292px; top: 0; width: 128px; height: 150px; }
  .card--back .name-plate {
    left: 250px; top: 62px; width: 170px; height: 48px;
    padding-left: 12px;
    font-size: 22px;
  }
  .card--back .brand-word--studio { left: 440px; top: 70px; font-size: 32px; }
  .card--back .brand-word--clinic { left: 450px; top: 128px; font-size: 20px; }

  .holder {
    position: absolute;
    left: 370px; top: 172px;
    color: var(--gold-text);
    white-space: nowrap;
  }
  .holder__name { font-size: 52px; line-height: 1; letter-spacing: 1px; }
  .holder__title {
    font-size: 13px; letter-spacing: 9px; margin-top: 4px; padding-left: 60px;
  }
  .contact {
    position: absolute;
    list-style: none;
    color: var(--gold-text);
    font-family: "Noto Sans", sans-serif;
    font-size: 28px;
    letter-spacing: 1px;
    white-space: nowrap;
  }
  .contact li { display: flex; align-items: center; gap: 16px; height: 46px; }
  .contact svg { width: 24px; height: 24px; flex: none; }
  .contact--phones { left: 56px; top: 220px; }
  .contact--online { left: 420px; top: 340px; }
</style>
</head>
<body>

<section class="card card--front" aria-label="Card front">
  <div class="gold-foil" role="img" aria-label="Gold foil texture background"></div>
  <div class="rule rule--top"></div>
  <div class="rule rule--bottom"></div>
  <div class="name-plate">dr Corbescu</div>
  <div class="brand-word brand-word--studio">studio</div>
  <div class="brand-word brand-word--clinic">dental clinic</div>
</section>

<section class="card card--back" aria-label="Card back">
  <div class="gold-foil" role="img" aria-label="Gold foil texture background"></div>
  <div class="name-plate">dr Corbescu</div>
  <div class="brand-word brand-word--studio">studio</div>
  <div class="brand-word brand-word--clinic">dental clinic</div>

  <div class="holder">
    <div class="holder__name">YourName</div>
    <div class="holder__title">TITLE</div>
  </div>

  <ul class="contact contact--phones">
    <li>
      <svg viewBox="0 0 24 24" aria-hidden="true"><rect x="6" y="2" width="12" height="20" rx="2" fill="none" stroke="var(--gold-text)" stroke-width="2"/><line x1="10" y1="18" x2="14" y2="18" stroke="var(--gold-text)" stroke-width="2"/></svg>
      <span>+1234567890</span>
    </li>
    <li>
      <svg viewBox="0 0 24 24" aria-hidden="true"><path d="M6 3l4 1 1 5-2 2c1 3 3 5 6 6l2-2 5 1 1 4-3 2C10 22 2 14 3 6z" fill="var(--gold-text)"/></svg>
      <span>+1234567890</span>
    </li>
  </ul>

  <ul class="contact contact--online">
    <li>
      <svg viewBox="0 0 24 24" aria-hidden="true"><rect x="2" y="5" width="20" height="14" fill="none" stroke="var(--gold-text)" stroke-width="2"/><path d="M2 5l10 8 10-8" fill="none" stroke="var(--gold-text)" stroke-width="2"/></svg>
      <span>yourmail@mail.com</span>
    </li>
    <li>
      <svg viewBox="0 0 24 24" aria-hidden="true"><circle cx="12" cy="12" r="10" fill="none" stroke="var(--gold-text)" stroke-width="2"/><ellipse cx="12" cy="12" rx="4" ry="10" fill="none" stroke="var(--gold-text)" stroke-width="1.5"/><line x1="2" y1="12" x2="22" y2="12" stroke="var(--gold-text)" stroke-width="1.5"/></svg>
      <span>www.yoursite.com</span>
    </li>
  </ul>
</section>

</body>
</html>
```